Brisk Fern

Rebrand current website and move it to BriskFern.com. Looking for a professional, eye catching, top 10 in World type website. My current website is: https://craftedbyoswin.sitebuilt.net/briskfern
I would like it moved to briskfern.com.

```html
<!DOCTYPE html>
<html lang="en">
<head>
<meta charset="utf-8">
<title>Brisk Fern — Music Producer Portfolio</title>
<link rel="stylesheet" href="https://fonts.googleapis.com/css2?family=Oswald:wght@500;600&family=Roboto:wght@400;500;700&display=swap">
<style>
:root{
  --stage:#e2e2e2;
  --blue:#0a66e4;
  --blue-deep:#0b4fc7;
  --ink:#111111;
  --footer:#150f0c;
}
*{box-sizing:border-box;margin:0;padding:0}
html,body{width:765px;height:1200px;overflow:hidden;background:var(--stage)}
body{position:relative;font-family:Roboto,Arial,sans-serif}
.site{
  --bg:#ffffff;--text:#111111;--muted:#666666;--card:#ffffff;--card-line:#e6e6e6;--dot:#9a9a9a;
  position:absolute;top:39px;width:325px;height:1126px;background:var(--bg);overflow:hidden;
  box-shadow:0 1px 4px rgba(0,0,0,.12);
}
.site--light{left:41px}
.site--dark{left:401px;--bg:#1b1b1b;--text:#ffffff;--muted:#e4e4e4;--card:#252525;--card-line:#2e2e2e;--dot:#ffffff}
section,header,footer{position:relative;width:325px}
.abs{position:absolute}
.heading{font-family:Oswald,Arial,sans-serif;font-weight:500;color:var(--text)}
.btn{position:absolute;background:var(--blue);color:#fff;font:700 3.6px/1 Roboto,sans-serif;display:flex;align-items:center;justify-content:center;letter-spacing:.1px}
.art{position:absolute}

/* header */
.topbar{height:18px;border-top:1.5px solid var(--blue);background:var(--bg)}
.brand{position:absolute;left:30px;top:2px;font:500 10.5px/14px Oswald,sans-serif;color:var(--text)}
.nav{position:absolute;right:30px;top:6.5px;display:flex;gap:4.5px;font:500 4px/5px Roboto,sans-serif;color:var(--text);align-items:center}
.nav .cart{color:var(--blue)}

/* hero */
.hero{height:162.5px}
.hero .art{inset:0;background:linear-gradient(120deg,#3a2a22 0%,#5a3a2c 30%,#2b2a30 55%,#1c2330 80%,#2a2420 100%)}
.hero .shade{position:absolute;inset:0;background:rgba(0,0,0,.35)}
.hero h1{position:absolute;top:59px;width:100%;text-align:center;font:600 9px/12px Oswald,sans-serif;color:#fff}
.hero p{position:absolute;top:74px;width:100%;text-align:center;font:400 5.8px/7px Roboto,sans-serif;color:#fff}
.hero .btn{left:148px;top:89px;width:29px;height:11.5px}
.social-rail{position:absolute;left:14px;top:70px;display:flex;flex-direction:column;gap:5px}
.social-rail span{width:3.5px;height:3.5px;border-radius:50%;background:#fff}
.pager{position:absolute;bottom:4.5px;left:0;width:100%;display:flex;justify-content:center;gap:2px}
.pager span{width:3px;height:3px;border:.6px solid #fff}
.pager span.on{background:var(--blue);border-color:#fff}

/* welcome */
.welcome{height:154.5px}
.welcome h2{position:absolute;left:30px;top:37px;font-size:8.6px;line-height:11px}
.welcome p{position:absolute;left:30px;top:55px;width:133px;font:400 3.9px/7.2px Roboto,sans-serif;color:var(--muted);text-align:justify}
.welcome .btn{left:30px;top:101px;width:41.5px;height:13px}
.portrait{position:absolute;left:192.5px;top:27px;width:100px;height:100px;border-radius:50%;background:radial-gradient(circle at 35% 35%,#8fd6cf 0%,#4d6a6a 40%,#2c2a28 80%);box-shadow:0 0 0 2px #fff,0 0 3px 2.5px rgba(0,0,0,.12)}
.reel{position:absolute;left:186px;top:91px;width:36px;height:36px;border-radius:50%;background:radial-gradient(circle at 40% 40%,#2f7ae8,#10308c);box-shadow:0 0 0 1.5px #fff}
.reel svg{position:absolute;left:11px;top:11px}

/* mixing */
.mixing{height:108px;display:flex}
.mixing .art{position:relative;width:162.5px;height:108px;background:linear-gradient(100deg,#2a1b14 0%,#6b4a33 40%,#3c2a20 70%,#1f150f 100%)}
.arrow{position:absolute;top:50px;width:9px;height:9px;background:#fff;display:flex;align-items:center;justify-content:center}
.mixing .panel{position:relative;width:162.5px;height:108px;background:var(--blue)}
.mixing h2{position:absolute;left:14.5px;top:14px;font:500 10px/13px Oswald,sans-serif;color:#fff}
.mixing p{position:absolute;left:14.5px;top:35px;width:118px;font:400 3.8px/6.7px Roboto,sans-serif;color:#fff;text-align:justify}
.mixing .btn{left:14.5px;top:78px;width:32px;height:12.5px;background:#fff;color:var(--blue)}

/* music */
.music{height:173.5px}
.section-title{position:absolute;top:23px;width:100%;text-align:center;font-size:9.6px;line-height:12px}
.player{position:absolute;left:30px;top:48px;width:265px;height:46.5px;background:var(--card);border:1px solid var(--card-line);box-shadow:0 0 2px rgba(0,0,0,.08)}
.player .track{position:absolute;left:16px;top:10px;font:400 5px/6px Roboto,sans-serif;color:var(--text)}
.player .bar{position:absolute;left:18px;top:23px;width:231px;height:.8px;background:var(--blue)}
.player .knob{position:absolute;left:15.5px;top:21px;width:4.5px;height:4.5px;border-radius:50%;background:var(--dot)}
.site--light .player .knob{background:#8d8d8d}
.player .time{position:absolute;left:16px;top:30px;font:400 3.8px/5px Roboto,sans-serif;color:var(--text)}
.player .controls{position:absolute;left:118px;top:29px;display:flex;gap:5px;align-items:center}
.player .vol{position:absolute;right:16px;top:29px}
.tracks{position:absolute;left:30px;top:105px;width:270px;height:36px}
.song{position:absolute;top:0;height:36px}
.song .thumb{position:absolute;left:0;top:0;width:34px;height:34px;background:linear-gradient(135deg,#c2883f,#7b4d8f 50%,#cfd6ea);box-shadow:0 0 0 1px #fff,0 0 2px 1px rgba(0,0,0,.15)}
.song .name{position:absolute;left:41px;top:2px;white-space:nowrap;font:500 5.6px/7px Roboto,sans-serif;color:var(--text)}
.song .stars{position:absolute;left:41px;top:10px;font:400 3.6px/4px Roboto,sans-serif;color:var(--blue);letter-spacing:.4px}
.song .btn{left:41px;top:21px;width:23px;height:9px}
.music .dots{position:absolute;top:147px;left:0;width:100%;display:flex;justify-content:center;gap:2px}
.music .dots span{width:3px;height:3px;background:var(--dot)}
.site--light .music .dots span{background:#a8a8a8}
.music .dots span.on{background:var(--blue)}

/* quote */
.quote{height:118.5px}
.quote .art{inset:0;background:linear-gradient(110deg,#141414 0%,#2a2520 35%,#1d2228 65%,#121212 100%)}
.quote blockquote{position:absolute;top:43px;width:100%;text-align:center;font:500 7.6px/10.5px Oswald,sans-serif;color:#fff}
.quote cite{position:absolute;top:71px;width:100%;text-align:center;font:700 5px/6px Roboto,sans-serif;color:var(--blue);font-style:normal}

/* blog */
.blog{height:181.5px}
.blog .section-title{top:24px}
.post{position:absolute;top:43px;width:86px;height:112px;background:var(--card);border:1px solid var(--card-line);box-shadow:0 0 2px rgba(0,0,0,.08)}
.post .art{left:1.5px;top:1.5px;width:82px;height:59px}
.post .date{position:absolute;left:3px;top:64px;font:400 4px/5px Roboto,sans-serif;color:var(--text);display:flex;gap:2.5px;align-items:center}
.post h3{position:absolute;left:3px;top:72px;width:80px;font:400 4.8px/7px Roboto,sans-serif;color:var(--blue)}
.post p{position:absolute;left:3px;top:87px;width:80px;font:400 3.7px/6px Roboto,sans-serif;color:var(--muted)}
.site--light .post p{color:#555}

/* contact */
.contact{height:122px}
.contact .art{inset:0;background:linear-gradient(180deg,#0b55d8 0%,#0a4fd0 50%,#0c5de0 100%)}
.contact h2{position:absolute;top:10px;width:100%;text-align:center;font:500 10px/13px Oswald,sans-serif;color:#fff}
.field{position:absolute;height:12px;background:#fff;font:400 3.9px/12px Roboto,sans-serif;color:#333;padding-left:4px}
.field.msg{line-height:10px;height:25px}
.contact .btn{left:134.5px;top:96px;width:56px;height:13px;background:var(--ink)}

/* footer */
.foot{height:86.5px;background:var(--footer)}
.foot .brand-foot{position:absolute;top:8.5px;width:100%;text-align:center;font:500 10px/13px Oswald,sans-serif;color:#fff}
.foot .icons{position:absolute;top:27px;width:100%;display:flex;justify-content:center;gap:4px}
.foot .icons span{width:9px;height:9px;background:#fff;display:flex;align-items:center;justify-content:center}
.foot .icons span i{width:3px;height:3px;border-radius:50%;background:var(--blue)}
.foot nav{position:absolute;top:44px;width:100%;text-align:center;font:400 5.3px/6px Roboto,sans-serif;color:#fff;word-spacing:1px}
.foot .info{position:absolute;top:58.5px;width:100%;display:flex;justify-content:center;gap:3px;align-items:center;font:500 3.8px/5px Roboto,sans-serif;color:#fff}
.foot .rule{position:absolute;left:30px;top:70px;width:265px;height:.5px;background:#5a5450}
.foot .copy{position:absolute;top:75px;width:100%;text-align:center;font:400 3.6px/5px Oswald,sans-serif;color:#fff}
.foot .chat{position:absolute;left:307px;top:66px}
.foot .tag{position:absolute;left:307px;top:76px;font:400 2.8px/3px Roboto,sans-serif;color:#ccc}
</style>
</head>
<body>

<!-- light theme -->
<div class="site site--light">
  <header class="topbar">
    <div class="brand">Brisk Fern</div>
    <div class="nav"><span>Home</span><span>Shop</span><span>Book Online</span><span>Blog</span><span>Contact Us</span><span>|</span>
      <svg width="4" height="4" viewBox="0 0 10 10"><circle cx="4" cy="4" r="3" fill="none" stroke="currentColor" stroke-width="1.6"/><path d="M6.3 6.3 9 9" stroke="currentColor" stroke-width="1.6"/></svg>
      <span class="cart">&#9635;(0)</span></div>
  </header>
  <section class="hero">
    <div class="art" role="img" aria-label="Producer working at a mixing desk in a brick-walled studio"></div>
    <div class="shade"></div>
    <div class="social-rail"><span></span><span></span><span></span></div>
    <h1>JOURNEY WITH OSWIN FERN</h1>
    <p>Music Producer Portfolio</p>
    <div class="btn">EXPLORE</div>
    <div class="pager"><span></span><span class="on"></span><span></span><span></span></div>
  </section>
  <section class="welcome">
    <h2 class="heading">Welcome To Oswin Fern</h2>
    <p>Hailing from Port Hallow, Oswin has always pushed himself to achieve more success in his music career. Looking to perfect his technical abilities and develop his own unique style, Oswin draws upon his Port Hallow roots and lifelong passion for music. Get in touch to learn more about his background, experience, and latest projects.</p>
    <div class="btn">CONTACT NOW</div>
    <div class="portrait" role="img" aria-label="Portrait photo of the producer"></div>
    <div class="reel" role="img" aria-label="Video preview thumbnail"><svg width="14" height="14" viewBox="0 0 14 14"><circle cx="7" cy="7" r="6" fill="none" stroke="#fff" stroke-width="1.2"/><path d="M5.5 4.5v5l4-2.5z" fill="#fff"/></svg></div>
  </section>
  <section class="mixing">
    <div class="art" role="img" aria-label="Studio condenser microphone with pop filter">
      <div class="arrow" style="left:1px"><svg width="4" height="5" viewBox="0 0 4 6"><path d="M3 .5 1 3l2 2.5" fill="none" stroke="#0a66e4" stroke-width=".8"/></svg></div>
      <div class="arrow" style="right:1px"><svg width="4" height="5" viewBox="0 0 4 6"><path d="M1 .5 3 3l-2 2.5" fill="none" stroke="#0a66e4" stroke-width=".8"/></svg></div>
    </div>
    <div class="panel">
      <h2>Mixing &amp; Mastering</h2>
      <p>Lorem ipsum dolor sit amet, consectetur adipiscing elit, sed do eiusmod tempor incididunt ut labore et dolore magna aliqua. Ut enim ad minim veniam, quis nostrud exercitation ullamco laboris nisi ut aliquip ex ea commodo consequat duis aute irure dolor in reprehenderit in voluptate velit esse cillum.</p>
      <div class="btn">BUY NOW</div>
    </div>
  </section>
  <section class="music">
    <h2 class="heading section-title">Music Album</h2>
    <div class="player">
      <div class="track">Oswin Trap Trap</div>
      <div class="bar"></div><div class="knob"></div>
      <div class="time">00:00 / 04.16</div>
      <div class="controls">
        <svg width="6" height="4" viewBox="0 0 12 8" fill="currentColor" style="color:var(--text)"><path d="M0 0h1.5v8H0zM6 0v8L1.5 4zM11.5 0v8L7 4z"/></svg>
        <svg width="6" height="6" viewBox="0 0 12 12" style="color:var(--text)"><circle cx="6" cy="6" r="5" fill="none" stroke="currentColor" stroke-width="1.3"/><path d="M4.8 3.6v4.8L8.6 6z" fill="currentColor"/></svg>
        <svg width="6" height="4" viewBox="0 0 12 8" fill="currentColor" style="color:var(--text)"><path d="M0 0v8l4.5-4zM5 0v8l4.5-4zM10.5 0H12v8h-1.5z"/></svg>
      </div>
      <svg class="vol" width="5" height="4" viewBox="0 0 10 8" style="color:var(--text)"><path d="M0 2.5h2L5 0v8L2 5.5H0z" fill="currentColor"/><path d="M6.5 2a3 3 0 0 1 0 4M8 .8a5 5 0 0 1 0 6.4" fill="none" stroke="currentColor" stroke-width=".9"/></svg>
    </div>
    <div class="tracks">
      <div class="song" style="left:0"><div class="thumb" role="img" aria-label="Album cover"></div><div class="name">Oswin Trap Trap</div><div class="stars">★★★★★</div><div class="btn">PLAY</div></div>
      <div class="song" style="left:98px"><div class="thumb" role="img" aria-label="Album cover"></div><div class="name">Oswin A list</div><div class="stars">★★★★★</div><div class="btn">PLAY</div></div>
      <div class="song" style="left:186px"><div class="thumb" role="img" aria-label="Album cover"></div><div class="name">Oswin Element</div><div class="stars">★★★★★</div><div class="btn">PLAY</div></div>
    </div>
    <div class="dots"><span></span><span class="on"></span><span></span><span></span></div>
  </section>
  <section class="quote">
    <div class="art" role="img" aria-label="Dim studio with headphones resting on a mixing console"></div>
    <blockquote>“Music expresses that which cannot be said and on which<br>it is impossible to be silent”</blockquote>
    <cite>- MARA QUILL -</cite>
  </section>
  <section class="blog">
    <h2 class="heading section-title">Latest Blog</h2>
    <article class="post" style="left:30px"><div class="art" role="img" aria-label="Guitarist recording with a laptop" style="background:linear-gradient(135deg,#6a4a3a,#2d2a2c 60%,#b08a70)"></div><div class="date"><svg width="4" height="4" viewBox="0 0 8 8"><rect x=".5" y="1" width="7" height="6.5" fill="none" stroke="#0a66e4"/><path d="M.5 3h7" stroke="#0a66e4"/></svg>23 Jan 2020</div><h3>5 Things the Artist Needs to Know Before Recording</h3><p>This is your blog post. Blogs are a great way to connect with your audience and keep them coming back.</p></article>
    <article class="post" style="left:119.5px"><div class="art" role="img" aria-label="Headphones on a mixing board" style="background:linear-gradient(135deg,#2a3a34,#4f7a74 50%,#1d2422)"></div><div class="date"><svg width="4" height="4" viewBox="0 0 8 8"><rect x=".5" y="1" width="7" height="6.5" fill="none" stroke="#0a66e4"/><path d="M.5 3h7" stroke="#0a66e4"/></svg>23 Jan 2020</div><h3>Recording Equipment Must-Haves for Every Studio</h3><p>This is your blog post. Great looking images make your blog posts more visually compelling for your audience,</p></article>
    <article class="post" style="left:209px"><div class="art" role="img" aria-label="Band rehearsing in a studio" style="background:linear-gradient(135deg,#7a5a44,#c9a27a 45%,#3c3440)"></div><div class="date"><svg width="4" height="4" viewBox="0 0 8 8"><rect x=".5" y="1" width="7" height="6.5" fill="none" stroke="#0a66e4"/><path d="M.5 3h7" stroke="#0a66e4"/></svg>23 Jan 2020</div><h3>Sound Check: Recording Tips from the Pros</h3><p>This is your blog post. To really engage your site visitors we suggest you blog about subjects that are related to your site</p></article>
  </section>
  <section class="contact">
    <div class="art" role="img" aria-label="Blue-tinted mixing console background"></div>
    <h2>Contact Us</h2>
    <div class="field" style="left:71px;top:33px;width:90px">Name</div>
    <div class="field" style="left:163.5px;top:33px;width:90px">Email</div>
    <div class="field" style="left:71px;top:48.5px;width:90px">Phone</div>
    <div class="field" style="left:163.5px;top:48.5px;width:90px">Subject</div>
    <div class="field msg" style="left:71px;top:64px;width:182.5px">Message</div>
    <div class="btn">SUBMIT NOW</div>
  </section>
  <footer class="foot">
    <div class="brand-foot">Oswin Fern</div>
    <div class="icons"><span><i></i></span><span><i></i></span><span><i></i></span></div>
    <nav>HOME &nbsp;| &nbsp;SHOP &nbsp;| &nbsp;BOOK ONLINE &nbsp;| &nbsp;BLOG &nbsp;| &nbsp;CONTACT US</nav>
    <div class="info"><svg width="3" height="3" viewBox="0 0 8 8"><path d="M1 0h2l1 2-1.2 1a5 5 0 0 0 2.2 2.2L6 4l2 1v2c-4 .5-8.5-4-8-7z" fill="#0a66e4"/></svg>555-013-2048 &nbsp;| <svg width="3.5" height="3" viewBox="0 0 8 6"><rect width="8" height="6" fill="#0a66e4"/><path d="M0 0l4 3 4-3" stroke="#fff" stroke-width=".7" fill="none"/></svg> hello@briskfern.com &nbsp;| <svg width="2.5" height="3.5" viewBox="0 0 6 8"><path d="M3 0a3 3 0 0 1 3 3c0 2-3 5-3 5S0 5 0 3a3 3 0 0 1 3-3z" fill="#0a66e4"/></svg> Port Hallow,Westmere</div>
    <div class="rule"></div>
    <div class="copy">© 2021 Oswin Fern. All Rights Reserved</div>
    <svg class="chat" width="8" height="7" viewBox="0 0 16 14"><path d="M2 1h9a2 2 0 0 1 2 2v4a2 2 0 0 1-2 2H6l-3 3V9H2a2 2 0 0 1-2-2V3a2 2 0 0 1 2-2z" fill="#0a66e4"/><path d="M14 5h0a2 2 0 0 1 2 2v3a2 2 0 0 1-2 2h-1v2l-2.5-2H8" fill="#0a66e4"/></svg>
    <div class="tag">C45</div>
  </footer>
</div>

<!-- dark theme -->
<div class="site site--dark">
  <header class="topbar">
    <div class="brand">Brisk Fern</div>
    <div class="nav"><span>Home</span><span>Shop</span><span>Book Online</span><span>Blog</span><span>Contact Us</span><span>|</span>
      <svg width="4" height="4" viewBox="0 0 10 10"><circle cx="4" cy="4" r="3" fill="none" stroke="currentColor" stroke-width="1.6"/><path d="M6.3 6.3 9 9" stroke="currentColor" stroke-width="1.6"/></svg>
      <span class="cart">&#9635;(0)</span></div>
  </header>
  <section class="hero">
    <div class="art" role="img" aria-label="Producer working at a mixing desk in a brick-walled studio"></div>
    <div class="shade"></div>
    <div class="social-rail"><span></span><span></span><span></span></div>
    <h1>JOURNEY WITH OSWIN FERN</h1>
    <p>Music Producer Portfolio</p>
    <div class="btn">EXPLORE</div>
    <div class="pager"><span></span><span class="on"></span><span></span><span></span></div>
  </section>
  <section class="welcome">
    <h2 class="heading">Welcome To Oswin Fern</h2>
    <p>Hailing from Port Hallow, Oswin has always pushed himself to achieve more success in his music career. Looking to perfect his technical abilities and develop his own unique style, Oswin draws upon his Port Hallow roots and lifelong passion for music. Get in touch to learn more about his background, experience, and latest projects.</p>
    <div class="btn">CONTACT NOW</div>
    <div class="portrait" role="img" aria-label="Portrait photo of the producer"></div>
    <div class="reel" role="img" aria-label="Video preview thumbnail"><svg width="14" height="14" viewBox="0 0 14 14"><circle cx="7" cy="7" r="6" fill="none" stroke="#fff" stroke-width="1.2"/><path d="M5.5 4.5v5l4-2.5z" fill="#fff"/></svg></div>
  </section>
  <section class="mixing">
    <div class="art" role="img" aria-label="Studio condenser microphone with pop filter">
      <div class="arrow" style="left:1px"><svg width="4" height="5" viewBox="0 0 4 6"><path d="M3 .5 1 3l2 2.5" fill="none" stroke="#0a66e4" stroke-width=".8"/></svg></div>
      <div class="arrow" style="right:1px"><svg width="4" height="5" viewBox="0 0 4 6"><path d="M1 .5 3 3l-2 2.5" fill="none" stroke="#0a66e4" stroke-width=".8"/></svg></div>
    </div>
    <div class="panel">
      <h2>Mixing &amp; Mastering</h2>
      <p>Lorem ipsum dolor sit amet, consectetur adipiscing elit, sed do eiusmod tempor incididunt ut labore et dolore magna aliqua. Ut enim ad minim veniam, quis nostrud exercitation ullamco laboris nisi ut aliquip ex ea commodo consequat duis aute irure dolor in reprehenderit in voluptate velit esse cillum.</p>
      <div class="btn">BUY NOW</div>
    </div>
  </section>
  <section class="music">
    <h2 class="heading section-title">Music Album</h2>
    <div class="player">
      <div class="track">Oswin Trap Trap</div>
      <div class="bar"></div><div class="knob"></div>
      <div class="time">00:00 / 04.16</div>
      <div class="controls">
        <svg width="6" height="4" viewBox="0 0 12 8" fill="currentColor" style="color:var(--text)"><path d="M0 0h1.5v8H0zM6 0v8L1.5 4zM11.5 0v8L7 4z"/></svg>
        <svg width="6" height="6" viewBox="0 0 12 12" style="color:var(--text)"><circle cx="6" cy="6" r="5" fill="none" stroke="currentColor" stroke-width="1.3"/><path d="M4.8 3.6v4.8L8.6 6z" fill="currentColor"/></svg>
        <svg width="6" height="4" viewBox="0 0 12 8" fill="currentColor" style="color:var(--text)"><path d="M0 0v8l4.5-4zM5 0v8l4.5-4zM10.5 0H12v8h-1.5z"/></svg>
      </div>
      <svg class="vol" width="5" height="4" viewBox="0 0 10 8" style="color:var(--text)"><path d="M0 2.5h2L5 0v8L2 5.5H0z" fill="currentColor"/><path d="M6.5 2a3 3 0 0 1 0 4M8 .8a5 5 0 0 1 0 6.4" fill="none" stroke="currentColor" stroke-width=".9"/></svg>
    </div>
    <div class="tracks">
      <div class="song" style="left:0"><div class="thumb" role="img" aria-label="Album cover"></div><div class="name">Oswin Trap Trap</div><div class="stars">★★★★★</div><div class="btn">PLAY</div></div>
      <div class="song" style="left:98px"><div class="thumb" role="img" aria-label="Album cover"></div><div class="name">Oswin A list</div><div class="stars">★★★★★</div><div class="btn">PLAY</div></div>
      <div class="song" style="left:186px"><div class="thumb" role="img" aria-label="Album cover"></div><div class="name">Oswin Element</div><div class="stars">★★★★★</div><div class="btn">PLAY</div></div>
    </div>
    <div class="dots"><span></span><span class="on"></span><span></span><span></span></div>
  </section>
  <section class="quote">
    <div class="art" role="img" aria-label="Dim studio with headphones resting on a mixing console"></div>
    <blockquote>“Music expresses that which cannot be said and on which<br>it is impossible to be silent”</blockquote>
    <cite>- MARA QUILL -</cite>
  </section>
  <section class="blog">
    <h2 class="heading section-title">Latest Blog</h2>
    <article class="post" style="left:30px"><div class="art" role="img" aria-label="Guitarist recording with a laptop" style="background:linear-gradient(135deg,#6a4a3a,#2d2a2c 60%,#b08a70)"></div><div class="date"><svg width="4" height="4" viewBox="0 0 8 8"><rect x=".5" y="1" width="7" height="6.5" fill="none" stroke="#0a66e4"/><path d="M.5 3h7" stroke="#0a66e4"/></svg>23 Jan 2020</div><h3>5 Things the Artist Needs to Know Before Recording</h3><p>This is your blog post. Blogs are a great way to connect with your audience and keep them coming back.</p></article>
    <article class="post" style="left:119.5px"><div class="art" role="img" aria-label="Headphones on a mixing board" style="background:linear-gradient(135deg,#2a3a34,#4f7a74 50%,#1d2422)"></div><div class="date"><svg width="4" height="4" viewBox="0 0 8 8"><rect x=".5" y="1" width="7" height="6.5" fill="none" stroke="#0a66e4"/><path d="M.5 3h7" stroke="#0a66e4"/></svg>23 Jan 2020</div><h3>Recording Equipment Must-Haves for Every Studio</h3><p>This is your blog post. Great looking images make your blog posts more visually compelling for your audience,</p></article>
    <article class="post" style="left:209px"><div class="art" role="img" aria-label="Band rehearsing in a studio" style="background:linear-gradient(135deg,#7a5a44,#c9a27a 45%,#3c3440)"></div><div class="date"><svg width="4" height="4" viewBox="0 0 8 8"><rect x=".5" y="1" width="7" height="6.5" fill="none" stroke="#0a66e4"/><path d="M.5 3h7" stroke="#0a66e4"/></svg>23 Jan 2020</div><h3>Sound Check: Recording Tips from the Pros</h3><p>This is your blog post. To really engage your site visitors we suggest you blog about subjects that are related to your site</p></article>
  </section>
  <section class="contact">
    <div class="art" role="img" aria-label="Blue-tinted mixing console background"></div>
    <h2>Contact Us</h2>
    <div class="field" style="left:71px;top:33px;width:90px">Name</div>
    <div class="field" style="left:163.5px;top:33px;width:90px">Email</div>
    <div class="field" style="left:71px;top:48.5px;width:90px">Phone</div>
    <div class="field" style="left:163.5px;top:48.5px;width:90px">Subject</div>
    <div class="field msg" style="left:71px;top:64px;width:182.5px">Message</div>
    <div class="btn">SUBMIT NOW</div>
  </section>
  <footer class="foot">
    <div class="brand-foot">Oswin Fern</div>
    <div class="icons"><span><i></i></span><span><i></i></span><span><i></i></span></div>
    <nav>HOME &nbsp;| &nbsp;SHOP &nbsp;| &nbsp;BOOK ONLINE &nbsp;| &nbsp;BLOG &nbsp;| &nbsp;CONTACT US</nav>
    <div class="info"><svg width="3" height="3" viewBox="0 0 8 8"><path d="M1 0h2l1 2-1.2 1a5 5 0 0 0 2.2 2.2L6 4l2 1v2c-4 .5-8.5-4-8-7z" fill="#0a66e4"/></svg>555-013-2048 &nbsp;| <svg width="3.5" height="3" viewBox="0 0 8 6"><rect width="8" height="6" fill="#0a66e4"/><path d="M0 0l4 3 4-3" stroke="#fff" stroke-width=".7" fill="none"/></svg> hello@briskfern.com &nbsp;| <svg width="2.5" height="3.5" viewBox="0 0 6 8"><path d="M3 0a3 3 0 0 1 3 3c0 2-3 5-3 5S0 5 0 3a3 3 0 0 1 3-3z" fill="#0a66e4"/></svg> Port Hallow,Westmere</div>
    <div class="rule"></div>
    <div class="copy">© 2021 Oswin Fern. All Rights Reserved</div>
    <svg class="chat" width="8" height="7" viewBox="0 0 16 14"><path d="M2 1h9a2 2 0 0 1 2 2v4a2 2 0 0 1-2 2H6l-3 3V9H2a2 2 0 0 1-2-2V3a2 2 0 0 1 2-2z" fill="#0a66e4"/><path d="M14 5h0a2 2 0 0 1 2 2v3a2 2 0 0 1-2 2h-1v2l-2.5-2H8" fill="#0a66e4"/></svg>
    <div class="tag">C45</div>
  </footer>
</div>

</body>
</html>
```